exciting cleaing project

I need a cleaning website built. It has to be built for a woman. the domain name is velmatidies.net.

I need the designer to find the images and code the site. the site needs to be about five pages.

here are some good examples:

https://www.brisktern.com/gainesville/

http://oakhollowtidy.com/

https://pebbleporchgainesville.com/services/

https://www.hubvox.com/housekeepers/gainesville-fl

https://glintrow.com/

Target Market(s)

home cleaning,

Industry/Entity Type

Cleaning Service

Coding

Coded - Design and coding required

Number of Pages Required

4 page

Font styles to use
Script

Colors
33a6d7
85acd3
f04a50
ec1f27

Requirements
Must have
• nice design
Nice to have
• residential
Should not have
• commercial

```html
<!DOCTYPE html>
<html lang="en">
<head>
<meta charset="utf-8">
<title>Velma Tidies — Home Cleaning</title>
<link href="https://fonts.googleapis.com/css2?family=Montserrat:wght@400;500;600;700;800&family=Open+Sans:ital,wght@0,400;0,600;0,700;1,400&display=swap" rel="stylesheet">
<style>
:root{
  --blue:#33a6d7;
  --blue-deep:#2b8fd0;
  --soft-blue:#85acd3;
  --red:#ec1f27;
  --red-soft:#f04a50;
  --ink:#1d1d1d;
  --text:#555;
  --footer:#262626;
  --line:#d9d9d9;
}
*{box-sizing:border-box;margin:0;padding:0}
html,body{width:1200px;height:3741px;overflow:hidden}
body{position:relative;background:#fff;font-family:"Open Sans",sans-serif;color:var(--text)}
.abs{position:absolute}
.heading{position:absolute;left:0;width:1200px;text-align:center;font-family:"Montserrat",sans-serif;font-size:40px;font-weight:700;color:var(--ink);letter-spacing:.5px}
.heading span{color:var(--blue-deep);font-weight:500}

/* header */
.site-header{left:0;top:0;width:1200px;height:92px;background:#fff;border-top:3px solid var(--blue-deep)}
.brand{left:145px;top:30px;display:flex;align-items:center;gap:8px;font-family:"Montserrat",sans-serif;font-size:32px;font-weight:600;color:var(--blue-deep);letter-spacing:.5px}
.brand i{width:22px;height:22px;border-radius:50%;background:var(--blue-deep);display:block}
.top-phone{left:728px;top:10px;display:flex;align-items:center;gap:8px;font-family:"Montserrat",sans-serif;font-size:26px;font-weight:600;color:var(--ink)}
.lang{left:960px;top:0;width:96px;height:28px;background:var(--blue-deep);color:#fff;font:700 12px "Montserrat",sans-serif;text-align:center;line-height:28px;clip-path:polygon(0 0,100% 0,88% 100%,0 100%)}
.nav{left:515px;top:56px;display:flex;gap:30px;font:600 14px "Montserrat",sans-serif;color:var(--ink)}
.nav .active{color:var(--blue-deep);position:relative}
.nav .active::after{content:"";position:absolute;left:-3px;right:-3px;top:26px;height:4px;background:var(--red)}

/* hero */
.hero{left:0;top:92px;width:1200px;height:666px;background:linear-gradient(160deg,#b9b3aa 0%,#8a8075 35%,#d4d0ca 55%,#4b4743 80%,#2b2a29 100%)}
.hero-title{left:0;top:148px;width:1200px;text-align:center;font:700 54px/1.12 "Montserrat",sans-serif;color:#fff;text-shadow:0 2px 6px rgba(0,0,0,.35)}
.hero-sub{left:0;top:285px;width:1200px;text-align:center;font:600 20px "Open Sans",sans-serif;color:#fff}
.btn-red{background:var(--red);color:#fff;border-radius:30px;font:700 18px "Montserrat",sans-serif;display:flex;align-items:center;justify-content:center;gap:10px}
.hero-btn{left:444px;top:338px;width:312px;height:56px}
.dots{left:558px;top:494px;display:flex;gap:7px}
.dots b{width:10px;height:10px;border-radius:50%;background:#fff}
.dots b.on{background:var(--blue)}
.infobar{left:145px;top:655px;width:910px;height:103px;background:rgba(25,25,25,.82);color:#fff;display:flex;align-items:center;justify-content:space-between;padding:0 40px}
.info{display:flex;align-items:center;gap:14px;font-size:11px;line-height:1.6}
.info strong{display:block;font:400 13px "Montserrat",sans-serif}
.info big{display:block;font:600 23px "Montserrat",sans-serif}

/* about */
.about-sub{left:0;top:902px;width:1200px;text-align:center;font:500 24px "Open Sans",sans-serif;color:var(--ink)}
.about-text{left:170px;top:948px;width:860px;text-align:center;font-size:14px;line-height:30px}
.blue-band{left:0;top:1196px;width:1200px;height:680px;background:linear-gradient(180deg,#3093d6,#3b9ed9)}
.video{left:262px;top:1062px;width:678px;height:370px;background:linear-gradient(120deg,#e9ecef,#c9d3da 45%,#a98a66 70%,#eef1f3);box-shadow:0 4px 16px rgba(0,0,0,.2)}
.play{left:556px;top:1195px}
.cats{left:0;top:1560px;width:1200px}
.cat{position:absolute;width:160px;text-align:center;color:#fff;font:600 16px/1.35 "Montserrat",sans-serif}
.cat svg{display:block;margin:0 auto 12px}

/* provide */
.service{position:absolute;width:293px}
.service .photo{height:180px}
.service .label{height:46px;display:flex;align-items:center;justify-content:center;color:#fff;font:700 15px "Montserrat",sans-serif;letter-spacing:.3px}
.view-more{left:497px;top:2235px;width:206px;height:56px;border:2px solid var(--blue-deep);border-radius:30px;color:var(--blue-deep);font:600 18px "Montserrat",sans-serif;display:flex;align-items:center;justify-content:center;gap:10px}

/* contact */
.contact-bg{left:0;top:2330px;width:1200px;height:582px;background:linear-gradient(180deg,#f1f1f1,#e7e5e2)}
.field{position:absolute;background:#fff;border:1px solid var(--line);font-size:13px;color:#777;padding:14px 18px}
.send{left:487px;top:2771px;width:225px;height:55px}

/* testimonials */
.quote{position:absolute;width:303px;height:182px;background:#fff;border:1px solid #ddd;box-shadow:0 3px 6px rgba(0,0,0,.08);text-align:center;padding:56px 30px 0;font-style:italic;font-size:11.5px;line-height:22px;color:#666}
.quote .mark{position:absolute;left:0;right:0;top:16px;font:700 46px/1 Georgia,serif;font-style:normal}
.author{position:absolute;display:flex;align-items:center;gap:8px}
.avatar{width:42px;height:42px;border-radius:50%;background:linear-gradient(135deg,#d8b39a,#7d5a48)}
.author strong{display:block;font:600 15px "Open Sans",sans-serif;color:#333}
.author small{display:block;font:600 10px "Open Sans",sans-serif;color:#333}
.badge{width:64px;height:26px;background:#cfcfcf;border-radius:4px;margin-left:16px}

/* footer */
.footer{left:0;top:3398px;width:1200px;height:343px;background:var(--footer);color:#ddd;font-size:12px;line-height:21px}
.fcol{position:absolute;top:50px}
.fcol h4{font:600 18px "Montserrat",sans-serif;color:var(--red);margin-bottom:10px}
.fcol li{list-style:none}
.fcol li::before{content:"» ";color:#fff}
.social{left:509px;top:238px;display:flex;gap:8px}
.social i{width:38px;height:38px;border-radius:50%;border:2px solid #fff;display:block}
.social i.on{background:var(--blue-deep);border-color:var(--blue-deep)}
.copy{left:0;top:302px;width:1200px;text-align:center;font-size:12px;color:#ddd}
</style>
</head>
<body>

<header class="abs site-header">
  <div class="abs brand"><i></i>VELMA TIDIES</div>
  <div class="abs top-phone">
    <svg width="32" height="32" viewBox="0 0 32 32"><circle cx="16" cy="16" r="14" fill="none" stroke="#2b8fd0" stroke-width="2"/><path d="M11 9l3 0 1 4-2 2c1 2 3 4 5 5l2-2 4 1 0 3c-1 1-2 1-3 1-6-1-11-6-12-12 0-1 1-2 2-2z" fill="#2b8fd0"/></svg>
    352-555-0148
  </div>
  <div class="abs lang">ENG/GR</div>
  <nav class="abs nav">
    <span class="active">HOME</span><span>ABOUT US</span><span>SERVICES</span><span>CLIENTS</span><span>LOCATIONS</span><span>CONTACT</span>
  </nav>
</header>

<section>
  <div class="abs hero" role="img" aria-label="Bright modern living room with white sofa, rug and lounge chair"></div>
  <h1 class="abs hero-title">HOMES, APARTMENTS,<br>CONDOS BUSINESS.</h1>
  <p class="abs hero-sub">Lorem ipsum dolor sitconsectetur adipiscing</p>
  <div class="abs btn-red hero-btn">REQUEST A FREE ESTIMATE
    <svg width="16" height="16" viewBox="0 0 16 16"><circle cx="8" cy="8" r="8" fill="#fff"/><path d="M6 4l4 4-4 4" stroke="#ec1f27" stroke-width="2.2" fill="none"/></svg></div>
  <div class="abs dots"><b></b><b></b><b class="on"></b><b></b><b></b></div>
  <div class="abs infobar">
    <div class="info">
      <svg width="52" height="52" viewBox="0 0 52 52"><circle cx="26" cy="26" r="23" fill="none" stroke="#fff" stroke-width="2"/><circle cx="26" cy="26" r="17" fill="none" stroke="#fff" stroke-width="1.5"/><path d="M26 15v11l-7 6" stroke="#fff" stroke-width="2" fill="none"/></svg>
      <div><strong>OPENING HOURS</strong>Contact By Text after 9am -10pm<br>Available Cleaning Time<br>Mon - Fri: 9am - 5pm</div>
    </div>
    <div class="info">
      <svg width="52" height="52" viewBox="0 0 52 52"><circle cx="26" cy="26" r="23" fill="none" stroke="#fff" stroke-width="2"/><path d="M18 14h6l2 7-3 3c2 4 5 7 9 9l3-3 7 2v6c-2 1-3 1-5 1-11-2-20-11-21-21 0-2 1-3 2-4z" fill="none" stroke="#fff" stroke-width="2"/></svg>
      <div><strong>CONTACT</strong><big>352-555-0148</big></div>
    </div>
    <div class="info">
      <svg width="52" height="40" viewBox="0 0 52 40"><rect x="2" y="4" width="48" height="32" fill="none" stroke="#fff" stroke-width="2"/><path d="M2 4l24 18L50 4M2 36l18-16M50 36L32 20" fill="none" stroke="#fff" stroke-width="2"/></svg>
      <div><strong>GET IN TOUCH WITH</strong>hello@velmatidies.net</div>
    </div>
  </div>
</section>

<section>
  <h2 class="heading" style="top:832px">ABOUT <span>VELMA TIDIES</span></h2>
  <p class="abs about-sub">Reliable &amp; Honest</p>
  <p class="abs about-text">Our mission at Velma’s Cleaning is simple: to provide high-quality services for our valued clients. Our team goes above and beyond to cater to each project’s specific needs. Throughopen communication and exceptional service, we hope you’ll find what you’re looking for with our House Cleaning Service. For more information or general inquiries, get in touch today.</p>
  <div class="abs blue-band"></div>
  <div class="abs video" role="img" aria-label="Cleaner in white shirt and blue gloves wiping a wooden shelf"></div>
  <svg class="abs play" width="88" height="88" viewBox="0 0 88 88"><circle cx="44" cy="44" r="40" fill="rgba(255,255,255,.85)" stroke="#333" stroke-width="6"/><path d="M36 28l22 16-22 16z" fill="#333"/></svg>
  <h2 class="heading" style="top:1478px;color:#fff">CATEGORIES</h2>
  <div class="abs cats">
    <div class="cat" style="left:122px;top:0">
      <svg width="114" height="114" viewBox="0 0 114 114"><circle cx="57" cy="57" r="54" fill="none" stroke="#fff" stroke-width="3"/><circle cx="57" cy="57" r="46" fill="none" stroke="#fff" stroke-width="2"/><path d="M32 72V46h50v26M32 62h50M40 56v-6h12v6M62 56v-6h12v6" fill="none" stroke="#fff" stroke-width="2.5"/></svg>BEDROOM<br>INTERIOR</div>
    <div class="cat" style="left:282px;top:0">
      <svg width="114" height="114" viewBox="0 0 114 114"><circle cx="57" cy="57" r="54" fill="none" stroke="#fff" stroke-width="3"/><circle cx="57" cy="57" r="46" fill="none" stroke="#fff" stroke-width="2"/><path d="M44 32h26v16H44zM40 52h34c0 10-6 16-17 16S40 62 40 52zM48 68l-2 10h22l-2-10" fill="none" stroke="#fff" stroke-width="2.5"/></svg>BATHROOMS</div>
    <div class="cat" style="left:440px;top:0">
      <svg width="114" height="114" viewBox="0 0 114 114"><circle cx="57" cy="57" r="54" fill="none" stroke="#fff" stroke-width="3"/><circle cx="57" cy="57" r="46" fill="none" stroke="#fff" stroke-width="2"/><path d="M32 34h50v12H32zM32 52h50v26H32zM57 52v26M38 60h12M64 60h12" fill="none" stroke="#fff" stroke-width="2.5"/></svg>KITCHEN</div>
    <div class="cat" style="left:599px;top:0">
      <svg width="114" height="114" viewBox="0 0 114 114"><circle cx="57" cy="57" r="54" fill="none" stroke="#fff" stroke-width="3"/><circle cx="57" cy="57" r="46" fill="none" stroke="#fff" stroke-width="2"/><path d="M38 54h38M57 54v22M30 44v32M84 44v32M30 62h10v14M84 62h-10v14" fill="none" stroke="#fff" stroke-width="2.5"/></svg>DINING ROOM</div>
    <div class="cat" style="left:758px;top:0">
      <svg width="114" height="114" viewBox="0 0 114 114"><circle cx="57" cy="57" r="54" fill="none" stroke="#fff" stroke-width="3"/><circle cx="57" cy="57" r="46" fill="none" stroke="#fff" stroke-width="2"/><path d="M42 50h30v16H42zM36 56h6v18h30V56h6v18M40 30v16M34 30h12" fill="none" stroke="#fff" stroke-width="2.5"/></svg>LIVING ROOM</div>
    <div class="cat" style="left:917px;top:0">
      <svg width="114" height="114" viewBox="0 0 114 114"><circle cx="57" cy="57" r="54" fill="none" stroke="#fff" stroke-width="3"/><circle cx="57" cy="57" r="46" fill="none" stroke="#fff" stroke-width="2"/><path d="M30 50h22v26M30 76V50M62 50h22v26M62 76V50M30 62h22M62 62h22M41 42v8M73 42v8" fill="none" stroke="#fff" stroke-width="2.5"/></svg>KIDS ROOMS</div>
  </div>
  <svg class="abs" style="left:0;top:1780px" width="1200" height="110" viewBox="0 0 1200 110"><path d="M0 70Q600-30 1200 70V110H0z" fill="#fff"/><path d="M0 70Q600-30 1200 70" fill="none" stroke="#2b8fd0" stroke-width="4"/></svg>
</section>

<section>
  <h2 class="heading" style="top:1873px">WHAT <span>WE PROVIDE</span></h2>
  <svg class="abs" style="left:86px;top:2030px" width="20" height="84" viewBox="0 0 20 84"><path d="M18 2L2 42l16 40" fill="none" stroke="#888" stroke-width="2"/></svg>
  <svg class="abs" style="left:1094px;top:2030px" width="20" height="84" viewBox="0 0 20 84"><path d="M2 2l16 40-16 40" fill="none" stroke="#888" stroke-width="2"/></svg>
  <div class="service" style="left:144px;top:1955px">
    <div class="photo" role="img" aria-label="Cleaner vacuuming a bright living room" style="background:linear-gradient(135deg,#eef0f0,#c8cbc9 60%,#6e8a72)"></div>
    <div class="label" style="background:#1f1f1f">WEEKLY, BI-WEEKLY, MONTHLY</div></div>
  <div class="service" style="left:454px;top:1955px">
    <div class="photo" role="img" aria-label="Woman in plaid shirt wiping a windowsill with yellow gloves" style="background:linear-gradient(135deg,#f3f2ee,#d9d3c8 55%,#b8533f)"></div>
    <div class="label" style="background:var(--red)">MOVE IN &amp; OUT CLEANING</div></div>
  <div class="service" style="left:763px;top:1955px">
    <div class="photo" role="img" aria-label="Woman in sun hat washing house windows outdoors" style="background:linear-gradient(135deg,#4e7a3a,#8c5b4a 50%,#b07a66)"></div>
    <div class="label" style="background:#1f1f1f">DEEP CLEANING</div></div>
  <div class="abs view-more">VIEW MORE
    <svg width="16" height="16" viewBox="0 0 16 16"><circle cx="8" cy="8" r="8" fill="#2b8fd0"/><path d="M6 4l4 4-4 4" stroke="#fff" stroke-width="2.2" fill="none"/></svg></div>
</section>

<section>
  <div class="abs contact-bg" role="img" aria-label="Soft faded interior with plants and cushions"></div>
  <svg class="abs" style="left:0;top:2300px" width="1200" height="90" viewBox="0 0 1200 90"><path d="M0 0H1200V10Q600 110 0 10z" fill="#fff"/><path d="M0 10Q600 110 1200 10" fill="none" stroke="#2b8fd0" stroke-width="4"/></svg>
  <h2 class="heading" style="top:2458px">GET <span>IN TOUCH</span></h2>
  <div class="field" style="left:172px;top:2530px;width:275px;height:47px">Name</div>
  <div class="field" style="left:462px;top:2530px;width:275px;height:47px">Email</div>
  <div class="field" style="left:752px;top:2530px;width:276px;height:47px">Subject</div>
  <div class="field" style="left:172px;top:2592px;width:420px;height:48px">Phone</div>
  <div class="field" style="left:607px;top:2592px;width:421px;height:48px">Address</div>
  <div class="field" style="left:172px;top:2654px;width:856px;height:92px">Message</div>
  <div class="abs btn-red send">SEND MESSAGE
    <svg width="16" height="16" viewBox="0 0 16 16"><circle cx="8" cy="8" r="8" fill="#fff"/><path d="M6 4l4 4-4 4" stroke="#ec1f27" stroke-width="2.2" fill="none"/></svg></div>
</section>

<section>
  <h2 class="heading" style="top:2985px">SATISFIED <span>CUSTOMERS</span></h2>
  <svg class="abs" style="left:78px;top:3140px" width="22" height="50" viewBox="0 0 22 50"><path d="M20 2L2 25l18 23" fill="none" stroke="#999" stroke-width="2"/></svg>
  <svg class="abs" style="left:1106px;top:3140px" width="22" height="50" viewBox="0 0 22 50"><path d="M2 2l18 23-18 23" fill="none" stroke="#999" stroke-width="2"/></svg>
  <div class="quote" style="left:135px;top:3073px"><span class="mark" style="color:var(--blue-deep)">“</span>In ullamcorper est eget tempor cursus neque mi consectetuer mi a ultricies massa est sed nisl Class aptent taciti sociosqu ad litora torquent per conubia nostra</div>
  <div class="quote" style="left:451px;top:3073px;border-color:var(--red-soft)"><span class="mark" style="color:var(--red)">“</span>In ullamcorper est eget tempor cursus neque mi consectetuer mi a ultricies massa est sed nisl Class aptent taciti sociosqu ad litora torquent per conubia nostra</div>
  <div class="quote" style="left:771px;top:3073px"><span class="mark" style="color:var(--blue-deep)">“</span>In ullamcorper est eget tempor cursus neque mi consectetuer mi a ultricies massa est sed nisl Class aptent taciti sociosqu ad litora torquent per conubia nostra</div>
  <div class="author" style="left:212px;top:3275px"><div class="avatar" role="img" aria-label="Customer portrait"></div><div><strong>By Author</strong><small>City, Location</small></div><div class="badge"></div></div>
  <div class="author" style="left:524px;top:3275px"><div class="avatar" role="img" aria-label="Customer portrait"></div><div><strong>By Author</strong><small>City, Location</small></div><div class="badge"></div></div>
  <div class="author" style="left:848px;top:3275px"><div class="avatar" role="img" aria-label="Customer portrait"></div><div><strong>By Author</strong><small>City, Location</small></div><div class="badge"></div></div>
</section>

<footer class="abs footer">
  <div class="fcol" style="left:160px">
    <h4>CONTACT US</h4>
    <p>&#9679; 233,Sed ut perspiciatis unde<br>&nbsp;&nbsp;&nbsp;omnis iste natus.</p>
    <p>&#9742; 352-555-0148</p>
    <p>&#9993; hello@velmatidies.net</p>
  </div>
  <div class="fcol" style="left:412px">
    <h4>OPENING HOURS</h4>
    <p>&#9719; Contact By Text after 9am -10pm<br>Available Cleaning Time<br>Sunday: By Appointment<br>Mon - Fri:9am - 5pm<br>Saturday- Sunday: Please Contact</p>
  </div>
  <div class="fcol" style="left:697px">
    <h4>QUICK LINKS</h4>
    <ul><li>Home</li><li>About us</li><li>Services</li><li>News</li><li>Locations</li><li>Contact us</li></ul>
  </div>
  <div class="fcol" style="left:916px">
    <h4>CATEGORIES</h4>
    <ul><li>Bedroom Interior</li><li>Bathrooms</li><li>Kitchen</li><li>Dining room</li><li>Living room</li><li>Kids rooms</li></ul>
  </div>
  <div class="abs social"><i></i><i class="on"></i><i></i><i></i></div>
  <p class="abs copy">Copyrights © 2019,Velma Tidies.All rights reserved &nbsp;|&nbsp; Privacy Policy</p>
</footer>

</body>
</html>
```